Vantrel - corporate Business Card

We need a good look and innovative business card for a new start up company based in Los Angeles called "Vantrel". We are in a payment business, including payment card, app, and ewallet. We are expert in online payment and Card not present (CNP) transaction.
We need an innovative, modern business card.

Our logo font is Aero Matics

Target Market(s)

Startup - Bank - Online Payment - Card Manufacturing

Industry/Entity Type

Startup

Contact Information for Business Card

phone: 555 371 6042 - Address: 4270 Marrowgate blvd, Harlow Park, CA 90418

Requirements
Must have
• Message: innovative, professional, expert, high tech, trust, online payment expert, security
Nice to have
• no comment
Should not have
• no Comment

```html
<!DOCTYPE html>
<html lang="en">
<head>
<meta charset="utf-8">
<title>Vantrel Business Card</title>
<link href="https://fonts.googleapis.com/css2?family=Montserrat:wght@400;500;700;800&display=swap" rel="stylesheet">
<style>
  :root {
    --brand-red: #b71f31;
    --card-white: #ffffff;
    --text-gray: #5a5a5a;
    --stage: #1c1c1e;
  }
  * { margin: 0; padding: 0; box-sizing: border-box; }
  html, body { width: 1200px; height: 900px; overflow: hidden; }
  body {
    background: var(--stage);
    font-family: "Montserrat", sans-serif;
    position: relative;
  }
  .card {
    position: absolute;
    left: 260px;
    width: 680px;
    height: 390px;
    border-radius: 26px;
    overflow: hidden;
  }
  /* Back side */
  .card-back {
    top: 50px;
    background: var(--brand-red);
  }
  .back-emblem {
    position: absolute;
    left: 50%;
    top: 70px;
    width: 200px;
    height: 200px;
    margin-left: -100px;
    border-radius: 50%;
    background: var(--card-white);
    display: flex;
    align-items: center;
    justify-content: center;
  }
  .back-emblem-name {
    color: var(--brand-red);
    font-weight: 800;
    font-size: 38px;
    letter-spacing: 0.5px;
  }
  .back-website {
    position: absolute;
    left: 0; right: 0;
    bottom: 42px;
    display: flex;
    justify-content: center;
    align-items: center;
    gap: 10px;
    color: var(--card-white);
    font-weight: 700;
    font-size: 17px;
    letter-spacing: 1px;
  }
  .back-website svg { width: 18px; height: 18px; }

  /* Front side */
  .card-front {
    top: 470px;
    background: var(--card-white);
  }
  .front-brand {
    position: absolute;
    left: 66px;
    top: 160px;
    display: flex;
    align-items: center;
    gap: 12px;
  }
  .brand-dot {
    width: 62px;
    height: 62px;
    border-radius: 50%;
    background: var(--brand-red);
  }
  .brand-name {
    color: var(--brand-red);
    font-weight: 700;
    font-size: 50px;
    letter-spacing: 0.5px;
    line-height: 1;
  }
  .front-divider {
    position: absolute;
    left: 372px;
    top: 100px;
    width: 2px;
    height: 190px;
    background: var(--brand-red);
  }
  .contact-block {
    position: absolute;
    left: 396px;
    top: 98px;
  }
  .person-name {
    color: var(--brand-red);
    font-weight: 800;
    font-size: 23px;
    line-height: 1.1;
  }
  .person-title {
    color: var(--text-gray);
    font-weight: 500;
    font-size: 16px;
    letter-spacing: 0.5px;
    margin-bottom: 10px;
  }
  .contact-list { list-style: none; }
  .contact-item {
    display: flex;
    align-items: flex-start;
    gap: 12px;
    color: var(--text-gray);
    font-size: 15px;
    font-weight: 500;
    line-height: 1.35;
    margin-bottom: 4px;
  }
  .contact-item svg {
    width: 14px;
    height: 14px;
    flex: none;
    margin-top: 3px;
    fill: var(--brand-red);
  }
  .contact-phone { letter-spacing: 1.5px; font-size: 16px; }
</style>
</head>
<body>

  <section class="card card-back" aria-label="Card back">
    <div class="back-emblem">
      <span class="back-emblem-name">Vantrel</span>
    </div>
    <div class="back-website">
      <svg viewBox="0 0 20 20" fill="none" stroke="#ffffff" stroke-width="1.5">
        <circle cx="10" cy="10" r="8"/>
        <ellipse cx="10" cy="10" rx="3.5" ry="8"/>
        <line x1="2" y1="10" x2="18" y2="10"/>
        <line x1="3.5" y1="6" x2="16.5" y2="6"/>
        <line x1="3.5" y1="14" x2="16.5" y2="14"/>
      </svg>
      <span>www.vantrel.la</span>
    </div>
  </section>

  <section class="card card-front" aria-label="Card front">
    <div class="front-brand">
      <span class="brand-dot"></span>
      <span class="brand-name">Vantrel</span>
    </div>
    <div class="front-divider"></div>
    <div class="contact-block">
      <p class="person-name">Dana Whitlock</p>
      <p class="person-title">President</p>
      <ul class="contact-list">
        <li class="contact-item contact-phone">
          <svg viewBox="0 0 16 16"><path d="M3.5 1.5l2.5 0 1 3.5-1.6 1.2c.8 1.8 2.2 3.2 4 4l1.2-1.6 3.5 1v2.5c0 .8-.7 1.4-1.5 1.4C6.8 13.5 2.5 9.2 2.1 3c0-.8.6-1.5 1.4-1.5z"/></svg>
          <span>555 371 6042</span>
        </li>
        <li class="contact-item contact-phone">
          <svg viewBox="0 0 16 16"><path d="M4.5 0.5h7c.6 0 1 .4 1 1v13c0 .6-.4 1-1 1h-7c-.6 0-1-.4-1-1v-13c0-.6.4-1 1-1zm.8 2v10h5.4v-10zm2.7 10.8a.7.7 0 100 1.4.7.7 0 000-1.4z"/></svg>
          <span>555 418 2937</span>
        </li>
        <li class="contact-item">
          <svg viewBox="0 0 16 16"><path d="M1 3h14v10H1zm1.3 1.2L8 8.6l5.7-4.4z"/></svg>
          <span>dana@vantrel.com</span>
        </li>
        <li class="contact-item">
          <svg viewBox="0 0 16 16"><path d="M8 0.5a5 5 0 00-5 5c0 3.8 5 10 5 10s5-6.2 5-10a5 5 0 00-5-5zm0 7a2 2 0 110-4 2 2 0 010 4z"/></svg>
          <span>4270 Marrowgate blvd<br>Harlow Park, CA 90418</span>
        </li>
      </ul>
    </div>
  </section>

</body>
</html>
```